Powerpoint template for Marlow Brook Consulting

I need a powerpoint template for my business that would also work for Google slides.
I intermittently deliver training to people and I want a nice powerpoint template, that could also work in google docs to help make production easier and more seamless for me. I also sometimes product reports and analyses that are best done in powerpoint or Google slides. I need a title page, Title and content page, section heading page and any other pages that someone normally has!

Target Market(s)

Leaders and managers in medium to large companies. I provide training and coaching services to senior staff who have got 'stuck' and want help to find their way forward.

Font styles to use
Sans Serif

Requirements
Must have
• Colours and fonts to fit with logo please.
• Must include the logo and company name.
Nice to have
• a picture for the front?

```html
<!DOCTYPE html>
<html lang="en">
<head>
<meta charset="utf-8">
<title>Marlow Brook Consulting – Presentation Template</title>
<link href="https://fonts.googleapis.com/css2?family=Open+Sans:wght@400;600;700&display=swap" rel="stylesheet">
<style>
:root{
  --teal:#1fb59b;
  --teal-dark:#17a396;
  --blue:#1b86a8;
  --blue-light:#8cc8dc;
  --navy:#2d4a8f;
  --purple:#4b2e91;
  --red:#ee2b2b;
  --ink:#1d1d1d;
  --text:#3a3a3a;
  --grey:#d6d6d6;
  --grey-light:#efefef;
  --beige:#e6e2cf;
  --dark:#2b2b2b;
  --page:#ffffff;
}
*{box-sizing:border-box;margin:0;padding:0}
html,body{width:1200px;height:2341px;overflow:hidden;background:var(--page)}
body{position:relative;font-family:"Open Sans",Arial,sans-serif;color:var(--text)}
.slide{position:absolute;background:#fff;overflow:hidden;box-shadow:0 0 0 1px #dcdcdc,0 1px 4px rgba(0,0,0,.12)}
.abs{position:absolute}
.title{position:absolute;font-weight:700;color:var(--ink);white-space:nowrap}
.title .accent{color:var(--teal)}
.body{font-size:7px;line-height:1.45;color:var(--text)}
.justify{text-align:justify}
.center{text-align:center}
.foot-line{position:absolute;left:14px;right:14px;bottom:14px;height:1px;background:var(--teal)}
.foot-brand{position:absolute;left:14px;bottom:4px;font-size:5.5px;font-weight:700;color:var(--purple);line-height:1.1;width:50px}
.foot-tab{position:absolute;right:18px;bottom:0;width:22px;height:14px;background:var(--teal);clip-path:polygon(0 35%,50% 0,100% 35%,100% 100%,0 100%)}
.brand-name{font-weight:600;color:var(--purple);text-align:center;line-height:1.15}
/* hero */
.hero-photo{position:absolute;inset:0;background:linear-gradient(120deg,#5b4a3e 0%,#8c7a6a 30%,#c9c2b8 55%,#6f6a66 80%,#3d3a38 100%)}
.hero-panel{position:absolute;left:184px;top:0;width:313px;height:355px;background:rgba(255,255,255,.72)}
/* feature boxes */
.feature{position:absolute;top:125px;width:125px;height:140px;background:var(--grey);padding:32px 10px 0}
.feature-icon{position:absolute;top:-22px;left:42px;width:42px;height:42px;border-radius:50%;background:#fff;border:2px solid #c8c8c8}
/* table */
.data-table{position:absolute;left:281px;top:167px;width:204px;border-collapse:collapse;font-size:5.5px}
.data-table th{background:var(--teal);color:#fff;font-weight:600;height:11px}
.data-table td{text-align:center;height:14px;border-bottom:1px solid #e5e5e5}
.data-table td.row-head{background:#f0f0f0}
/* process */
.step-band{position:absolute;top:136px;height:31px;color:#fff;font-size:10px;font-weight:700;display:flex;align-items:center;justify-content:center}
.step-num{position:absolute;width:38px;height:38px;border-radius:50%;color:#fff;font-weight:700;font-size:18px;display:flex;align-items:center;justify-content:center}
.step-text{position:absolute;width:104px;font-size:7px;line-height:1.45;text-align:center}
/* numbered grid */
.num-item{position:absolute;width:125px;display:flex;gap:6px}
.num-item .n{font-size:18px;line-height:1;color:var(--ink)}
.num-item h4{font-size:7px;font-weight:700;color:var(--ink);margin-bottom:3px}
.num-item p{font-size:6.3px;line-height:1.4}
/* list rows */
.tag{position:absolute;left:28px;width:100px;height:27px;color:#fff;font-size:7.5px;font-weight:700;display:flex;align-items:center;padding-left:10px}
.tag-bar{position:absolute;left:128px;width:256px;height:27px;background:var(--grey-light);font-size:5px;line-height:1.4;padding:6px 10px}
/* money boxes */
.money{position:absolute;top:125px;width:53px;height:39px;background:var(--teal);color:#fff;font-size:6.5px;font-weight:700;text-align:center;padding-top:5px}
.money::after{content:"";position:absolute;left:21px;bottom:-6px;border:6px solid transparent;border-bottom:0;border-top-color:var(--teal)}
/* points */
.points{position:absolute;top:129px;width:182px;height:154px;background:var(--beige)}
.points-head{height:15px;color:#fff;font-size:6px;font-weight:700;display:flex;align-items:center;justify-content:center}
.point{display:flex;gap:6px;padding:7px 8px 0}
.point .dot{flex:none;width:11px;height:11px;border-radius:50%;border:1.5px solid}
.point h5{font-size:6px;font-weight:700}
.point p{font-size:5px;color:#8a8a8a;line-height:1.3}
/* bars */
.pill{position:absolute;top:92px;width:25px;height:167px;border-radius:13px;background:#d9d9d9;overflow:hidden}
.pill-fill{position:absolute;left:0;right:0;bottom:0;border-radius:13px}
.pill-label{position:absolute;width:29px;height:29px;border-radius:50%;color:#fff;font-size:8px;font-weight:700;display:flex;align-items:center;justify-content:center;border:2px solid #fff}
/* contact */
.contact{position:absolute;left:385px;width:120px;text-align:center;color:#fff;font-size:8px;font-weight:600}
.contact svg{display:block;margin:0 auto 8px}
</style>
</head>
<body>

<!-- Cover -->
<section class="slide" style="left:223px;top:28px;width:706px;height:403px">
  <div class="hero-photo" role="img" aria-label="Photo of smiling colleagues giving a high five in a bright office"></div>
  <div class="hero-panel">
    <div class="abs" style="left:135px;top:70px;width:44px;height:44px;border-radius:50%;background:var(--teal)"></div>
    <div class="abs brand-name" style="left:10px;top:150px;width:293px;font-size:40px">Marlow Brook Consulting</div>
  </div>
</section>

<!-- About -->
<section class="slide" style="left:20px;top:446px;width:560px;height:315px">
  <h2 class="title" style="left:72px;top:48px;font-size:22px">About <span class="accent">Company</span></h2>
  <div class="abs body center" style="left:30px;top:112px;width:268px">
    <p>Lorem ipsum dolor sit amet, consectetur adipiscing elit, sed do eiusmod tempor incididunt ut labore et dolore magna aliqua. Ut enim ad minim veniam, quis nostrud exercitation ullamco laboris nisi ut aliquip ex ea commodo consequat. Lorem ipsum dolor sit amet, consectetur adipiscing elit, sed do eiusmod tempor incididunt ut labore et dolore magna aliqua.</p>
    <p style="margin-top:9px">Lorem ipsum dolor sit amet, consectetur adipiscing elit, sed do eiusmod tempor incididunt ut labore et dolore magna aliqua. Ut enim ad minim veniam, quis nostrud exercitation ullamco laboris nisi ut.</p>
    <p style="margin-top:9px">Aliquip ex ea commodo consequat. Lorem ipsum dolor sit amet, consectetur adipiscing elit, sed do eiusmod tempor incididunt ut labore et dolore magna aliqua.</p>
  </div>
  <div class="abs" style="left:405px;top:55px;width:40px;height:40px;border-radius:50%;background:var(--teal)"></div>
  <div class="abs brand-name" style="left:335px;top:112px;width:180px;font-size:27px">Marlow Brook Consulting</div>
  <div class="foot-line"></div><div class="foot-brand">Marlow Brook Consulting</div><div class="foot-tab"></div>
</section>

<!-- Two column text -->
<section class="slide" style="left:616px;top:446px;width:557px;height:315px">
  <h2 class="title" style="left:22px;top:135px;font-size:19px">Lorem ipsum <span class="accent">dolor</span></h2>
  <div class="abs body justify" style="left:234px;top:50px;width:138px">
    <p>Lorem ipsum dolor sit amet, consectetur adipiscing elit, sed do eiusmod tempor incididunt ut labore et dolore magna aliqua. Ut enim ad minim veniam, quis nostrud exercitation ullamco laboris nisi ut aliquip ex ea commodo consequat. Lorem ipsum dolor sit amet, sed do</p>
    <p style="margin-top:12px">Lorem ipsum dolor sit amet, consectetur adipiscing elit, sed do eiusmod tempor incididunt ut labore et dolore magna aliqua. Ut enim ad minim veniam, quis nostrud exercitation ullamco laboris nisi ut aliquip ex ea commodo consequat. Lorem ipsum dolor sit amet, consectetur adipiscing elit, sed do eiusmod tempor incididunt ut labore et dolore magna aliqua.</p>
  </div>
  <div class="abs body justify" style="left:393px;top:50px;width:138px">
    <p>Lorem ipsum dolor sit amet, consectetur adipiscing elit, sed do eiusmod tempor incididunt ut labore et dolore magna aliqua. Ut enim ad minim veniam, quis nostrud exercitation ullamco laboris nisi ut aliquip ex ea commodo consequat. Lorem ipsum dolor sit amet,</p>
    <p style="margin-top:12px">Lorem ipsum dolor sit amet, consectetur adipiscing elit, sed do eiusmod tempor incididunt ut labore et dolore magna aliqua. Ut enim ad minim veniam, quis nostrud exercitation ullamco laboris nisi ut aliquip ex ea commodo consequat. Lorem ipsum dolor sit amet, consectetur adipiscing elit, sed do eiusmod tempor incididunt ut labore et dolore magna aliqua.</p>
  </div>
  <div class="foot-line"></div><div class="foot-brand">Marlow Brook Consulting</div><div class="foot-tab"></div>
</section>

<!-- Three features -->
<section class="slide" style="left:20px;top:776px;width:560px;height:312px">
  <h2 class="title" style="left:0;right:0;top:16px;font-size:19px;text-align:center">Lorem ipsum <span class="accent">dolor</span></h2>
  <p class="abs body center" style="left:130px;top:44px;width:300px">Lorem ipsum dolor sit amet, consectetur adipiscing elit, sed do eiusmod tempor incididunt ut labore et dolore magna aliqua.</p>
  <div class="feature" style="left:78px">
    <svg class="feature-icon" viewBox="0 0 42 42"><circle cx="21" cy="21" r="9" fill="none" stroke="#1fb59b" stroke-width="4" stroke-dasharray="3 2.6"/><circle cx="21" cy="21" r="6" fill="none" stroke="#1fb59b" stroke-width="2"/></svg>
    <p class="body justify" style="color:#fff">Lorem ipsum dolor sit amet, consectetur adipiscing elit, sed do eiusmod tempor incididunt ut labore et dolore magna aliqua. Lorem ipsum dolor sit amet, consectetur adipiscing elit, sed do eiusmod tempor incididunt ut labore et dolore magna aliqua.</p>
  </div>
  <div class="feature" style="left:217px">
    <svg class="feature-icon" viewBox="0 0 42 42"><circle cx="21" cy="21" r="10" fill="none" stroke="#1fb59b" stroke-width="2"/><circle cx="21" cy="21" r="5.5" fill="none" stroke="#1fb59b" stroke-width="2"/><circle cx="21" cy="21" r="1.8" fill="#1fb59b"/><path d="M21 21 L30 12" stroke="#1fb59b" stroke-width="2"/></svg>
    <p class="body justify" style="color:#fff">Lorem ipsum dolor sit amet, consectetur adipiscing elit, sed do eiusmod tempor incididunt ut labore et dolore magna aliqua. Lorem ipsum dolor sit amet, consectetur adipiscing elit, sed do eiusmod tempor incididunt ut labore et dolore magna aliqua.</p>
  </div>
  <div class="feature" style="left:355px">
    <svg class="feature-icon" viewBox="0 0 42 42"><g fill="#1fb59b"><rect x="12" y="22" width="4" height="8"/><rect x="18" y="18" width="4" height="12"/><rect x="24" y="14" width="4" height="16"/></g><path d="M11 12 L30 26" stroke="#1fb59b" stroke-width="1.5"/></svg>
    <p class="body justify" style="color:#fff">Lorem ipsum dolor sit amet, consectetur adipiscing elit, sed do eiusmod tempor incididunt ut labore et dolore magna aliqua. Lorem ipsum dolor sit amet, consectetur adipiscing elit, sed do eiusmod tempor incididunt ut labore et dolore magna aliqua.</p>
  </div>
  <div class="foot-line"></div><div class="foot-brand">Marlow Brook Consulting</div><div class="foot-tab"></div>
</section>

<!-- Text and table -->
<section class="slide" style="left:616px;top:776px;width:557px;height:312px">
  <h2 class="title" style="left:0;right:0;top:48px;font-size:19px;text-align:center">Lorem ipsum <span class="accent">dolor</span></h2>
  <p class="abs body center" style="left:68px;top:84px;width:420px">Lorem ipsum dolor sit amet, consectetur adipiscing elit, sed do eiusmod tempor incididunt ut labore et dolore magna aliqua. Lorem ipsum dolor sit amet, consectetur adipiscing elit, sed do eiusmod tempor incididunt ut labore et dolore magna aliqua.</p>
  <div class="abs" style="left:36px;top:145px;width:472px;height:86px;border:2px solid var(--teal);border-radius:10px"></div>
  <div class="abs" style="left:55px;top:137px;width:148px;height:18px;border-radius:9px;background:var(--teal);color:#fff;font-size:9px;font-weight:700;display:flex;align-items:center;justify-content:center">Lorem ipsum dolor</div>
  <p class="abs body" style="left:50px;top:163px;width:222px">Lorem ipsum dolor sit amet, consectetur adipiscing elit, sed do eiusmod tempor incididunt ut labore et dolore magna aliqua. Lorem ipsum dolor sit amet, consectetur adipiscing elit, sed do eiusmod tempor incididunt ut labore et dolore magna aliqua.</p>
  <table class="data-table">
    <tr><th></th><th>Text</th><th>Text</th><th>Text</th></tr>
    <tr><td class="row-head">Add Text</td><td>Text</td><td>Text</td><td>Text</td></tr>
    <tr><td class="row-head">Add Text</td><td>Text</td><td>Text</td><td>Text</td></tr>
  </table>
  <div class="foot-line"></div><div class="foot-brand">Marlow Brook Consulting</div><div class="foot-tab"></div>
</section>

<!-- Process -->
<section class="slide" style="left:20px;top:1105px;width:560px;height:315px">
  <div class="step-band" style="left:11px;width:133px;background:var(--teal)">Lorem ipsum dolor</div>
  <div class="step-band" style="left:148px;width:131px;background:var(--blue)">Lorem ipsum dolor</div>
  <div class="step-band" style="left:287px;width:130px;background:var(--purple)">Lorem ipsum dolor</div>
  <div class="step-band" style="left:423px;width:131px;background:var(--teal)">Lorem ipsum dolor</div>
  <svg class="abs" style="left:0;top:0" width="560" height="315">
    <path d="M30 136 L36 126 L42 136Z" fill="#1fb59b"/>
    <path d="M160 167 L166 177 L172 167Z" fill="#1b86a8"/>
    <path d="M302 136 L308 126 L314 136Z" fill="#4b2e91"/>
    <path d="M443 167 L449 177 L455 167Z" fill="#1fb59b"/>
  </svg>
  <div class="step-num" style="left:17px;top:78px;background:var(--teal)">1</div>
  <div class="step-num" style="left:147px;top:192px;background:var(--blue)">2</div>
  <div class="step-num" style="left:289px;top:78px;background:var(--purple)">3</div>
  <div class="step-num" style="left:430px;top:192px;background:var(--teal)">4</div>
  <p class="step-text" style="left:20px;top:180px">Lorem ipsum dolor sit amet, consectetur adipiscing elit, sed do eiusmod tempor incididunt ut labore et dolore magna aliqua.</p>
  <p class="step-text" style="left:162px;top:58px">Lorem ipsum dolor sit amet, consectetur adipiscing elit, sed do eiusmod tempor incididunt ut labore et dolore magna aliqua.</p>
  <p class="step-text" style="left:300px;top:180px">Lorem ipsum dolor sit amet, consectetur adipiscing elit, sed do eiusmod tempor incididunt ut labore et dolore magna aliqua.</p>
  <p class="step-text" style="left:440px;top:58px">Lorem ipsum dolor sit amet, consectetur adipiscing elit, sed do eiusmod tempor incididunt ut labore et dolore magna aliqua.</p>
  <div class="foot-line"></div><div class="foot-brand">Marlow Brook Consulting</div><div class="foot-tab"></div>
</section>

<!-- Numbered grid -->
<section class="slide" style="left:613px;top:1105px;width:560px;height:315px">
  <h2 class="title" style="left:0;right:0;top:20px;font-size:20px;text-align:center">Lorem ipsum <span class="accent">dolor</span></h2>
  <div class="num-item" style="left:84px;top:80px"><span class="n">01</span><div><h4>Lorem ipsum dolor</h4><p>Lorem ipsum dolor sit amet, consectetur adipiscing elit, sed do eiusmod tempor incididunt ut labore et dolore magna aliqua.</p></div></div>
  <div class="num-item" style="left:221px;top:80px"><span class="n">02</span><div><h4>Lorem ipsum dolor</h4><p>Lorem ipsum dolor sit amet, consectetur adipiscing elit, sed do eiusmod tempor incididunt ut labore et dolore magna aliqua.</p></div></div>
  <div class="num-item" style="left:360px;top:80px"><span class="n">03</span><div><h4>Lorem ipsum dolor</h4><p>Lorem ipsum dolor sit amet, consectetur adipiscing elit, sed do eiusmod tempor incididunt ut labore et dolore magna aliqua.</p></div></div>
  <div class="num-item" style="left:84px;top:156px"><span class="n">05</span><div><h4>Lorem ipsum dolor</h4><p>Lorem ipsum dolor sit amet, consectetur adipiscing elit, sed do eiusmod tempor incididunt ut labore et dolore magna aliqua.</p></div></div>
  <div class="num-item" style="left:221px;top:156px"><span class="n">06</span><div><h4>Lorem ipsum dolor</h4><p>Lorem ipsum dolor sit amet, consectetur adipiscing elit, sed do eiusmod tempor incididunt ut labore et dolore magna aliqua.</p></div></div>
  <div class="num-item" style="left:360px;top:156px"><span class="n">07</span><div><h4>Lorem ipsum dolor</h4><p>Lorem ipsum dolor sit amet, consectetur adipiscing elit, sed do eiusmod tempor incididunt ut labore et dolore magna aliqua.</p></div></div>
  <div class="abs" style="left:0;right:0;bottom:0;height:68px;background:var(--dark);color:#fff;font-size:13px;font-weight:700;text-align:center;line-height:1.4;padding-top:14px">Lorem ipsum dolor sit amet, consectetur adipiscing elit,<br>sed do eiusmod tempor</div>
</section>

<!-- Labelled rows -->
<section class="slide" style="left:0;top:1436px;width:413px;height:229px">
  <h2 class="title" style="left:123px;top:30px;font-size:15px">Lorem ipsum <span class="accent">dolor</span></h2>
  <div class="tag" style="top:87px;background:var(--blue)">Lorem ipsum dolor</div>
  <div class="tag-bar" style="top:87px">Lorem ipsum dolor sit amet, consectetur adipiscing elit, sed do eiusmod tempor incididunt ut labore et dolore magna aliqua.</div>
  <div class="tag" style="top:125px;background:var(--teal)">Lorem ipsum dolor</div>
  <div class="tag-bar" style="top:125px">Lorem ipsum dolor sit amet, consectetur adipiscing elit, sed do eiusmod tempor incididunt ut labore et dolore magna aliqua.</div>
  <div class="tag" style="top:164px;background:var(--blue-light)">Lorem ipsum dolor</div>
  <div class="tag-bar" style="top:164px">Lorem ipsum dolor sit amet, consectetur adipiscing elit, sed do eiusmod tempor incididunt ut labore et dolore magna aliqua.</div>
  <div class="foot-line"></div><div class="foot-brand">Marlow Brook Consulting</div><div class="foot-tab"></div>
</section>

<!-- Wheel -->
<section class="slide" style="left:413px;top:1436px;width:395px;height:229px">
  <svg class="abs" style="left:0;top:0" width="395" height="229">
    <g stroke="#fff" stroke-width="3">
      <path d="M106.7 133.1 A94 94 0 0 1 118 47.1 L160.6 76.9 A42 42 0 0 0 155.5 115.4Z" fill="#1fb59b"/>
      <path d="M118 47.1 A94 94 0 0 1 195 7 L195 59 A42 42 0 0 0 160.6 76.9Z" fill="#17a396"/>
      <path d="M195 7 A94 94 0 0 1 272 47.1 L229.4 76.9 A42 42 0 0 0 195 59Z" fill="#1fb59b"/>
      <path d="M272 47.1 A94 94 0 0 1 283.3 133.1 L234.5 115.4 A42 42 0 0 0 229.4 76.9Z" fill="#17a396"/>
    </g>
    <circle cx="195" cy="101" r="31" fill="#17a396" stroke="#fff" stroke-width="3"/>
    <g fill="none" stroke="#fff" stroke-width="2">
      <circle cx="195" cy="93" r="7"/><path d="M181 116 Q195 98 209 116"/>
      <circle cx="163.6" cy="40.7" r="6" stroke-dasharray="2.4 1.6" stroke-width="3.5"/><circle cx="163.6" cy="40.7" r="3"/>
      <path d="M217 33 h18 v12 h-10 l-5 4 v-4 h-3z"/>
      <circle cx="127.6" cy="89" r="7"/><path d="M124.6 97 v5 h6 v-5"/>
      <path d="M253 94 L271 84 L265 102 L261 95Z"/>
    </g>
  </svg>
  <span class="abs" style="left:55px;top:20px;font-size:7px;font-weight:700;color:var(--ink)">1. Lorem ipsum dolor</span>
  <span class="abs" style="left:261px;top:20px;font-size:7px;font-weight:700;color:var(--ink)">3. Lorem ipsum dolor</span>
  <span class="abs" style="left:12px;top:108px;font-size:7px;font-weight:700;color:var(--ink)">2. Lorem ipsum dolor</span>
  <span class="abs" style="left:296px;top:108px;font-size:7px;font-weight:700;color:var(--ink)">4. Lorem ipsum dolor</span>
  <h2 class="title" style="left:0;right:0;top:170px;font-size:17px;text-align:center">Lorem ipsum <span class="accent">dolor</span></h2>
</section>

<!-- Values on photo -->
<section class="slide" style="left:808px;top:1436px;width:392px;height:229px">
  <div class="abs" style="left:0;top:0;width:392px;height:140px;background:linear-gradient(135deg,#4a4440,#2e2b2a 60%,#5a544e)" role="img" aria-label="Darkened photo of a team working around a desk with laptops"></div>
  <h2 class="title" style="left:0;right:0;top:52px;font-size:15px;text-align:center;color:#fff;padding-left:70px">Lorem ipsum dolor</h2>
  <div class="money" style="left:59px"><svg width="12" height="12" viewBox="0 0 12 12"><circle cx="6" cy="6" r="3.5" fill="none" stroke="#fff" stroke-width="2" stroke-dasharray="1.6 1.2"/></svg><br>$30,000</div>
  <div class="money" style="left:134px"><svg width="12" height="12" viewBox="0 0 12 12"><circle cx="5" cy="5" r="3.3" fill="none" stroke="#fff" stroke-width="1.5"/><path d="M7.5 7.5 L11 11" stroke="#fff" stroke-width="1.5"/></svg><br>$40,000</div>
  <div class="money" style="left:206px"><svg width="12" height="12" viewBox="0 0 12 12"><path d="M1 4 h3 l6 -3 v10 l-6 -3 h-3z" fill="#fff"/></svg><br>$50,000</div>
  <div class="money" style="left:268px"><svg width="12" height="12" viewBox="0 0 12 12"><circle cx="6" cy="3.5" r="2.5" fill="#fff"/><path d="M1.5 11 Q6 4 10.5 11z" fill="#fff"/></svg><br>$60,000</div>
  <p class="abs center" style="left:28px;top:182px;width:336px;font-size:5px;line-height:1.4">Lorem ipsum dolor sit amet, consectetur adipiscing elit, sed do eiusmod tempor incididunt ut labore et dolore magna aliqua. Lorem ipsum dolor sit amet, consectetur adipiscing elit, sed do eiusmod tempor incididunt ut labore et dolore magna aliqua. Lorem ipsum dolor sit amet, consectetur elit.</p>
  <div class="foot-line" style="bottom:8px"></div><div class="foot-tab"></div>
</section>

<!-- Illustration with text -->
<section class="slide" style="left:20px;top:1678px;width:557px;height:314px">
  <div class="abs" style="left:27px;top:16px;width:226px;height:257px;border-radius:40% 40% 50% 50%;background:radial-gradient(circle at 50% 70%,#e6e6ea 0%,#d6cfe6 45%,#f4f2f8 75%)" role="img" aria-label="Illustration of three colleagues collaborating around a table with laptops"></div>
  <h2 class="title" style="left:287px;top:22px;font-size:20px">Lorem ipsum <span class="accent">dolor</span></h2>
  <div class="abs" style="left:287px;top:72px;width:255px">
    <h3 style="font-size:9px;font-weight:700;color:var(--ink);margin-bottom:4px">Lorem ipsum dolor</h3>
    <p class="body" style="font-size:6.5px">Lorem ipsum dolor sit amet, consectetur adipiscing elit, sed do eiusmod tempor incididunt ut labore et dolore magna aliqua. Lorem ipsum dolor sit amet, consectetur adipiscing elit, sed do eiusmod tempor incididunt ut labore et dolore magna aliqua.</p>
  </div>
  <div class="abs" style="left:287px;top:136px;width:255px">
    <h3 style="font-size:9px;font-weight:700;color:var(--ink);margin-bottom:4px">Lorem ipsum dolor</h3>
    <p class="body" style="font-size:6.5px">Lorem ipsum dolor sit amet, consectetur adipiscing elit, sed do eiusmod tempor incididunt ut labore et dolore magna aliqua. Lorem ipsum dolor sit amet, consectetur adipiscing elit, sed do eiusmod tempor incididunt ut labore et dolore magna aliqua.</p>
  </div>
  <div class="abs" style="left:287px;top:198px;width:255px">
    <h3 style="font-size:9px;font-weight:700;color:var(--ink);margin-bottom:4px">Lorem ipsum dolor</h3>
    <p class="body" style="font-size:6.5px">Lorem ipsum dolor sit amet, consectetur adipiscing elit, sed do eiusmod tempor incididunt ut labore et dolore magna aliqua. Lorem ipsum dolor sit amet, consectetur adipiscing elit, sed do eiusmod tempor incididunt ut labore et dolore magna aliqua.</p>
  </div>
  <div class="foot-line"></div><div class="foot-brand">Marlow Brook Consulting</div><div class="foot-tab"></div>
</section>

<!-- Pros and cons -->
<section class="slide" style="left:613px;top:1678px;width:560px;height:314px">
  <h2 class="title" style="left:0;right:0;top:30px;font-size:20px;text-align:center">Lorem ipsum <span class="accent">dolor</span></h2>
  <svg class="abs" style="left:0;top:0" width="560" height="130">
    <circle cx="180" cy="102" r="19" fill="none" stroke="#1fb59b" stroke-width="3"/>
    <path d="M171 102 L178 109 L190 95" fill="none" stroke="#1fb59b" stroke-width="3.5"/>
    <circle cx="381" cy="102" r="19" fill="none" stroke="#ee2b2b" stroke-width="3"/>
    <path d="M373 94 L389 110 M389 94 L373 110" stroke="#ee2b2b" stroke-width="3.5"/>
  </svg>
  <div class="points" style="left:89px">
    <div class="points-head" style="background:var(--teal)">POSITIVE POINTS</div>
    <div class="point"><span class="dot" style="border-color:var(--teal)"></span><div><h5 style="color:var(--teal)">TITLE GOES HERE</h5><p>This is a sample text. You simply add your own text and description here.</p></div></div>
    <div class="point"><span class="dot" style="border-color:var(--teal)"></span><div><h5 style="color:var(--teal)">TITLE GOES HERE</h5><p>This is a sample text. You simply add your own text and description here.</p></div></div>
    <div class="point"><span class="dot" style="border-color:var(--teal)"></span><div><h5 style="color:var(--teal)">TITLE GOES HERE</h5><p>This is a sample text. You simply add your own text and description here.</p></div></div>
    <div class="point"><span class="dot" style="border-color:var(--teal)"></span><div><h5 style="color:var(--teal)">TITLE GOES HERE</h5><p>This is a sample text. You simply add your own text and description here.</p></div></div>
  </div>
  <div class="points" style="left:292px">
    <div class="points-head" style="background:var(--red)">NEGATIVE POINTS</div>
    <div class="point"><span class="dot" style="border-color:var(--red)"></span><div><h5 style="color:var(--red)">TITLE GOES HERE</h5><p>This is a sample text. You simply add your own text and description here.</p></div></div>
    <div class="point"><span class="dot" style="border-color:var(--red)"></span><div><h5 style="color:var(--red)">TITLE GOES HERE</h5><p>This is a sample text. You simply add your own text and description here.</p></div></div>
    <div class="point"><span class="dot" style="border-color:var(--red)"></span><div><h5 style="color:var(--red)">TITLE GOES HERE</h5><p>This is a sample text. You simply add your own text and description here.</p></div></div>
    <div class="point"><span class="dot" style="border-color:var(--red)"></span><div><h5 style="color:var(--red)">TITLE GOES HERE</h5><p>This is a sample text. You simply add your own text and description here.</p></div></div>
  </div>
  <div class="foot-line"></div><div class="foot-brand">Marlow Brook Consulting</div><div class="foot-tab"></div>
</section>

<!-- Charts -->
<section class="slide" style="left:20px;top:2007px;width:557px;height:314px">
  <h2 class="title" style="left:0;right:0;top:30px;font-size:20px;text-align:center">Lorem ipsum <span class="accent">dolor</span></h2>
  <svg class="abs" style="left:0;top:0" width="160" height="220">
    <path d="M79 154 L79 103 A51 51 0 1 1 37.7 184Z" fill="#1fb59b"/>
    <path d="M79 154 L37.7 184 A51 51 0 0 1 37.7 124Z" fill="#4b2e91"/>
    <path d="M79 154 L37.7 124 A51 51 0 0 1 79 103Z" fill="#2d4a8f"/>
    <g fill="#fff" font-family="Open Sans, sans-serif" font-weight="700" text-anchor="middle">
      <text x="105" y="172" font-size="14">65</text>
      <text x="52" y="165" font-size="12">20</text>
      <text x="63" y="126" font-size="11">15</text>
    </g>
  </svg>
  <div class="abs center" style="left:179px;top:84px;width:136px"><h4 style="font-size:6.5px;font-weight:700;color:var(--ink);margin-bottom:4px">Lorem ipsum dolor</h4><p class="body" style="font-size:6.2px">Lorem ipsum dolor sit amet, consectetur adipiscing elit, sed do eiusmod tempor incididunt ut labore et dolore magna aliqua.</p></div>
  <div class="abs center" style="left:179px;top:151px;width:136px"><h4 style="font-size:6.5px;font-weight:700;color:var(--ink);margin-bottom:4px">Lorem ipsum dolor</h4><p class="body" style="font-size:6.2px">Lorem ipsum dolor sit amet, consectetur adipiscing elit, sed do eiusmod tempor incididunt ut labore et dolore magna aliqua.</p></div>
  <div class="abs center" style="left:179px;top:216px;width:136px"><h4 style="font-size:6.5px;font-weight:700;color:var(--ink);margin-bottom:4px">Lorem ipsum dolor</h4><p class="body" style="font-size:6.2px">Lorem ipsum dolor sit amet, consectetur adipiscing elit, sed do eiusmod tempor incididunt ut labore et dolore magna aliqua.</p></div>
  <div class="pill" style="left:350px"><div class="pill-fill" style="height:55%;background:var(--purple)"></div></div>
  <div class="pill" style="left:389px"><div class="pill-fill" style="height:80%;background:var(--blue)"></div></div>
  <div class="pill" style="left:428px"><div class="pill-fill" style="height:60%;background:var(--navy)"></div></div>
  <div class="pill" style="left:468px"><div class="pill-fill" style="height:90%;background:var(--teal)"></div></div>
  <div class="pill-label" style="left:348px;top:240px;background:var(--purple)">55%</div>
  <div class="pill-label" style="left:387px;top:240px;background:var(--blue)">80%</div>
  <div class="pill-label" style="left:426px;top:240px;background:var(--navy)">60%</div>
  <div class="pill-label" style="left:466px;top:240px;background:var(--teal)">90%</div>
  <div class="foot-line"></div><div class="foot-brand">Marlow Brook Consulting</div><div class="foot-tab"></div>
</section>

<!-- Contact -->
<section class="slide" style="left:613px;top:2007px;width:565px;height:314px">
  <div class="abs" style="inset:0;background:linear-gradient(135deg,#3c3c3c,#262626 55%,#343331)" role="img" aria-label="Darkened photo of a handshake over a desk"></div>
  <div class="abs" style="left:116px;top:80px;width:36px;height:36px;border-radius:50%;background:var(--teal)"></div>
  <div class="abs brand-name" style="left:20px;top:130px;width:232px;font-size:26px">Marlow Brook Consulting</div>
  <div class="abs" style="left:281px;top:69px;width:1px;height:215px;background:#fff"></div>
  <div class="contact" style="top:20px">
    <svg width="26" height="26" viewBox="0 0 26 26" fill="none" stroke="#fff" stroke-width="1.6"><circle cx="13" cy="13" r="11"/><ellipse cx="13" cy="13" rx="5" ry="11"/><path d="M2 13h22M4 7h18M4 19h18"/></svg>
    www.marlowbrook.co
  </div>
  <div class="contact" style="top:90px">
    <svg width="26" height="26" viewBox="0 0 26 26"><path d="M6 2 L10 2 L12 8 L9 10 Q12 16 16 17 L18 14 L24 16 L24 20 Q22 24 18 24 Q4 20 2 6 Q2 2 6 2Z" fill="#fff"/></svg>
    +1 555 0100 200
  </div>
  <div class="contact" style="top:160px">
    <svg width="28" height="22" viewBox="0 0 28 22"><rect x="1" y="1" width="26" height="20" rx="2" fill="#fff"/><path d="M2 3 L14 12 L26 3" fill="none" stroke="#2b2b2b" stroke-width="1.8"/></svg>
    hello@marlowbrook.co
  </div>
  <div class="contact" style="top:228px">
    <svg width="22" height="28" viewBox="0 0 22 28"><path d="M11 1 C5 1 1 5.5 1 11 C1 18 11 27 11 27 C11 27 21 18 21 11 C21 5.5 17 1 11 1Z" fill="#fff"/><circle cx="11" cy="11" r="4" fill="#2b2b2b"/></svg>
    2500 Brook Lane, Marlow<br>Street, USA
  </div>
</section>

</body>
</html>
```